Consulting firm business card, email signature, stationery
Halverton Advisory Group
Use standard fonts
Same font or standard is fine
Peter L. Dravik
President
842 S. Tolliver Street
Fairhollow, ST 00412
pete.dravik@halvertonag.example
halvertonag.example
The font can be standard for a professional consulting firm, or you can try with matching the logo.
The business card and email signature are most important. Stationery would be a nice bonus.
Ai version of logo file

```html
<!DOCTYPE html>
<html lang="en">
<head>
<meta charset="utf-8">
<title>Halverton Advisory Group – Business Card</title>
<link href="https://fonts.googleapis.com/css2?family=Crimson+Text:wght@400;600;700&display=swap" rel="stylesheet">
<style>
  :root {
    --page-bg: #ecebe8;
    --card-white: #ffffff;
    --ink-dark: #3d3d3d;
    --ink-grey: #5a5a5a;
    --brand-blue: #1f4e9c;
    --brand-blue-dark: #163a7a;
    --brand-orange: #f26a12;
    --brand-orange-light: #ff9a2a;
    --brand-orange-deep: #e2530a;
    --divider: #c9c9c9;
  }
  * { box-sizing: border-box; margin: 0; padding: 0; }
  html, body { width: 1200px; height: 850px; overflow: hidden; }
  body {
    background: var(--page-bg);
    font-family: "Crimson Text", Georgia, serif;
    display: flex;
    align-items: center;
    justify-content: center;
    gap: 40px;
  }
  .card {
    position: relative;
    width: 540px;
    height: 309px;
    overflow: hidden;
    box-shadow: 0 6px 18px rgba(0,0,0,0.18);
  }

  /* Back side */
  .card-back {
    background: radial-gradient(circle at 60% 45%, var(--brand-orange-light) 0%, var(--brand-orange) 45%, var(--brand-orange-deep) 100%);
  }
  .card-back .wordmark {
    position: absolute;
    left: 180px;
    top: 128px;
    display: flex;
    align-items: center;
    gap: 12px;
  }
  .card-back .wordmark-dot {
    width: 30px; height: 30px; border-radius: 50%;
    background: rgba(255,255,255,0.85);
  }
  .card-back .wordmark-name {
    color: #ffffff;
    font-weight: 600;
    font-size: 19px;
    letter-spacing: 1.5px;
    text-transform: uppercase;
    line-height: 1.1;
  }

  /* Front side */
  .card-front { background: var(--card-white); }
  .front-logo {
    position: absolute;
    left: 36px;
    top: 78px;
    display: flex;
    align-items: center;
    gap: 12px;
    width: 270px;
  }
  .front-logo-dot {
    flex: none;
    width: 46px; height: 46px; border-radius: 50%;
    background: var(--brand-orange);
  }
  .front-logo-name {
    color: var(--ink-dark);
    font-weight: 600;
    font-size: 21px;
    letter-spacing: 1.5px;
    text-transform: uppercase;
    line-height: 1.05;
  }
  .divider {
    position: absolute;
    left: 318px;
    top: 74px;
    width: 1px;
    height: 96px;
    background: var(--divider);
  }
  .contact-list {
    position: absolute;
    left: 330px;
    top: 78px;
    list-style: none;
    font-size: 11.5px;
    color: var(--ink-grey);
  }
  .contact-list li {
    display: flex;
    align-items: center;
    gap: 8px;
    height: 22px;
  }
  .contact-list svg { width: 12px; height: 12px; fill: var(--ink-dark); flex: none; }
  .person {
    position: absolute;
    left: 58px;
    top: 196px;
  }
  .person-name {
    color: var(--brand-blue);
    font-weight: 700;
    font-size: 20px;
    line-height: 1.1;
  }
  .person-title {
    color: var(--brand-orange);
    font-size: 14px;
    margin-left: 112px;
    line-height: 1.2;
  }
  .person-address {
    color: var(--ink-grey);
    font-size: 12.5px;
    line-height: 1.35;
    margin-top: 4px;
  }
  .corner-bands {
    position: absolute;
    left: 0; top: 0;
    width: 540px; height: 309px;
  }
  .corner-mark {
    position: absolute;
    right: 26px;
    top: 214px;
    width: 22px; height: 22px; border-radius: 50%;
    background: var(--brand-orange);
  }
</style>
</head>
<body>

  <section class="card card-back" aria-label="Card back">
    <div class="wordmark">
      <span class="wordmark-dot"></span>
      <span class="wordmark-name">Halverton<br>Advisory Group</span>
    </div>
  </section>

  <section class="card card-front" aria-label="Card front">
    <svg class="corner-bands" viewBox="0 0 540 309" aria-hidden="true">
      <polygon points="520,150 540,150 540,309 520,309" fill="var(--brand-orange)"/>
      <polygon points="230,309 540,262 540,309" fill="var(--brand-blue)"/>
      <polygon points="330,309 540,280 540,309" fill="var(--brand-blue-dark)"/>
    </svg>

    <div class="front-logo">
      <span class="front-logo-dot"></span>
      <span class="front-logo-name">Halverton<br>Advisory Group</span>
    </div>

    <div class="divider"></div>

    <ul class="contact-list">
      <li>
        <svg viewBox="0 0 24 24"><path d="M6.6 10.8a15.1 15.1 0 0 0 6.6 6.6l2.2-2.2a1 1 0 0 1 1-.25 11.4 11.4 0 0 0 3.6.57 1 1 0 0 1 1 1V20a1 1 0 0 1-1 1A17 17 0 0 1 3 4a1 1 0 0 1 1-1h3.5a1 1 0 0 1 1 1c0 1.25.2 2.45.57 3.57a1 1 0 0 1-.25 1z"/></svg>
        555-201-0142
      </li>
      <li>
        <svg viewBox="0 0 24 24"><path d="M7 1h10a2 2 0 0 1 2 2v18a2 2 0 0 1-2 2H7a2 2 0 0 1-2-2V3a2 2 0 0 1 2-2zm0 3v14h10V4zm5 15.5a1.2 1.2 0 1 0 0 2.4 1.2 1.2 0 0 0 0-2.4z"/></svg>
        555-201-0187
      </li>
      <li>
        <svg viewBox="0 0 24 24"><path d="M2 5h20v14H2zm2 2v.5l8 5 8-5V7zm0 2.8V17h16V9.8l-8 5z"/></svg>
        pete.dravik@halvertonag.example
      </li>
      <li>
        <svg viewBox="0 0 24 24"><path d="M12 2a10 10 0 1 0 0 20 10 10 0 0 0 0-20zm0 2c.9 1.2 1.6 2.6 2 4h-4c.4-1.4 1.1-2.8 2-4zM4.3 14a8 8 0 0 1 0-4h3.4a16 16 0 0 0 0 4zm.8 2h3c.3 1.3.8 2.5 1.4 3.6A8 8 0 0 1 5.1 16zm3-8h-3a8 8 0 0 1 4.4-3.6C7.9 5.5 7.4 6.7 7.1 8zM12 20c-.9-1.2-1.6-2.6-2-4h4c-.4 1.4-1.1 2.8-2 4zm2.3-6H9.7a14 14 0 0 1 0-4h4.6a14 14 0 0 1 0 4zm.2 5.6c.6-1.1 1.1-2.3 1.4-3.6h3a8 8 0 0 1-4.4 3.6zm1.8-5.6a16 16 0 0 0 0-4h3.4a8 8 0 0 1 0 4zm-.4-6c-.3-1.3-.8-2.5-1.4-3.6A8 8 0 0 1 18.9 8z"/></svg>
        www.halvertonag.example
      </li>
    </ul>

    <div class="person">
      <p class="person-name">Peter L. Dravik</p>
      <p class="person-title">President</p>
      <p class="person-address">842 S. Tolliver Street<br>Fairhollow, ST 00412</p>
    </div>

    <span class="corner-mark"></span>
  </section>

</body>
</html>
```